STATIONERY and Brand ID for KelvaBank

We need a family of identical Brand guide
Call Card
Envelope
Letterhead
Poster
Brochure

It needs to have an international Fee/

The ARCHITECTURE/STRUCTURE must show the highest level of creativity

1. Call card could be two sided
2. cal card can have a a flap
3. Call card can have a curved edge

Target Market(s)

Business and bank clients

Industry/Entity Type

Bank

Requirements
Must have
• the logo atatched
• the colour scheme must be used
• There must be a common look and feel and they must have the same DNA

```html
<!DOCTYPE html>
<html lang="en">
<head>
<meta charset="utf-8">
<title>KelvaBank Stationery</title>
<link rel="stylesheet" href="https://fonts.googleapis.com/css2?family=Roboto:wght@400;700&family=Roboto+Condensed:wght@500&display=swap">
<style>
  :root {
    --backdrop: #c5dee6;
    --navy: #052873;
    --navy-faint: #1a3a80;
    --cd-blue: #00329a;
    --lime: #7ec70d;
    --white: #ffffff;
    --ink: #111111;
  }
  html, body { margin: 0; padding: 0; overflow: hidden; }
  body { width: 1200px; height: 1199px; background: var(--backdrop); }
  .sheet { display: block; width: 1200px; height: 1199px; }
  .brand { font-family: "Roboto", sans-serif; font-weight: 700; letter-spacing: -1px; }
  .body-text { font-family: "Roboto", sans-serif; }
  .label { font-family: "Roboto Condensed", sans-serif; font-weight: 500; font-size: 23px; fill: var(--ink); }
</style>
</head>
<body>
<svg class="sheet" viewBox="0 0 1500 1500" xmlns="http://www.w3.org/2000/svg">
  <defs>
    <filter id="drop" x="-10%" y="-10%" width="120%" height="130%">
      <feDropShadow dx="0" dy="3" stdDeviation="3" flood-color="#000" flood-opacity="0.55"/>
    </filter>
    <linearGradient id="pageCurl" x1="0" x2="1" y1="0" y2="0">
      <stop offset="0" stop-color="#b8b8bc"/>
      <stop offset="0.35" stop-color="#f4f4f4"/>
      <stop offset="1" stop-color="#ffffff"/>
    </linearGradient>
    <linearGradient id="discTone" x1="0" y1="0" x2="1" y2="1">
      <stop offset="0.45" stop-color="var(--navy)"/>
      <stop offset="0.46" stop-color="var(--cd-blue)"/>
    </linearGradient>
  </defs>

  <!-- Compliment slip -->
  <g class="compliment-slip">
    <rect x="82" y="124" width="618" height="291" fill="var(--white)" filter="url(#drop)"/>
    <rect x="638" y="124" width="14" height="245" fill="var(--navy)"/>
    <rect x="638" y="369" width="14" height="46" fill="var(--lime)"/>
    <text class="brand" x="110" y="184" font-size="36" fill="var(--navy)">KelvaBank</text>
    <text class="body-text" x="620" y="182" font-size="24" text-anchor="end" fill="var(--navy)">With <tspan fill="var(--lime)">compliments</tspan></text>
    <rect class="contact-pill" x="116" y="321" width="21" height="94" rx="10" fill="var(--navy)"/>
    <g class="contact-icons" fill="var(--white)">
      <path d="M122,350 l4.5,-4 l4.5,4 v3 h-9z"/>
      <rect x="123" y="365" width="6" height="7" rx="2"/>
      <circle cx="126.5" cy="380" r="3.5"/>
      <rect x="122" y="388" width="9" height="6"/>
      <rect x="122" y="398" width="9" height="7"/>
    </g>
    <g class="body-text" font-size="8" fill="var(--ink)">
      <text x="149" y="351">P O Box 412, Port Selwyn</text>
      <text x="149" y="360">Isle of Carrowmere</text>
      <text x="149" y="372">1 (555) 210 3390</text>
      <text x="149" y="383">www.kelvabank.example</text>
      <text x="149" y="394">m.delaney@kelvabank.example</text>
      <text x="149" y="405">1 (555) 210 3391</text>
    </g>
    <text class="body-text" x="621" y="398" font-size="20" font-weight="700" text-anchor="end" fill="var(--navy)">Marcus Delaney</text>
    <text class="body-text" x="621" y="409" font-size="9" text-anchor="end" fill="var(--ink)">General Manager - Isle of Carrowmere</text>
  </g>

  <!-- Envelope -->
  <g class="envelope">
    <rect x="800" y="124" width="620" height="291" fill="var(--navy)" filter="url(#drop)"/>
    <text class="brand" x="1370" y="187" font-size="36" text-anchor="end" fill="var(--white)">KelvaBank</text>
    <text class="brand" transform="translate(876,392) rotate(-90)" font-size="52" fill="var(--navy-faint)">KelvaBank</text>
  </g>

  <!-- Folder open -->
  <g class="folder-open">
    <rect class="inside-panel" x="448" y="657" width="470" height="665" fill="var(--navy)"/>
    <path class="inner-page" d="M448,657 L683,657 C675,760 670,850 640,950 C600,1050 510,1100 470,1322 L448,1322 Z" fill="url(#pageCurl)" filter="url(#drop)"/>
    <path class="cover-flap" d="M448,657 L215,657 C110,657 50,740 50,825 C50,900 85,945 120,968 C60,990 25,1050 25,1110 L25,1200 C25,1280 100,1322 215,1322 L448,1322 Z" fill="var(--navy)"/>
    <text class="brand" x="152" y="843" font-size="50" fill="var(--white)">KelvaBank</text>
    <g class="disc">
      <circle cx="207" cy="1133" r="150" fill="url(#discTone)" stroke="var(--white)" stroke-width="2"/>
      <circle cx="207" cy="1133" r="54" fill="none" stroke="var(--navy)" stroke-width="2"/>
      <circle cx="207" cy="1133" r="30" fill="var(--navy)" stroke="var(--white)" stroke-width="2"/>
      <text class="brand" x="277" y="1139" font-size="15" fill="var(--white)" letter-spacing="-0.5">KelvaBank</text>
    </g>
    <path class="disc-pocket" d="M25,1112 C150,1170 300,1210 448,1218 L448,1322 L215,1322 C100,1322 25,1280 25,1200 Z" fill="var(--white)" filter="url(#drop)"/>
  </g>

  <!-- Folder closed -->
  <g class="folder-closed">
    <rect x="996" y="657" width="469" height="665" fill="var(--navy)"/>
    <path class="front-cover" d="M996,657 L1230,657 C1330,657 1395,720 1395,825 C1395,890 1370,935 1325,968 C1390,1000 1418,1060 1418,1130 C1418,1250 1350,1322 1230,1322 L996,1322 Z" fill="var(--white)" filter="url(#drop)"/>
    <rect x="1032" y="657" width="22" height="600" fill="var(--navy)"/>
    <rect x="1032" y="1257" width="22" height="65" fill="var(--lime)"/>
    <text class="brand" x="1067" y="729" font-size="40" fill="var(--navy)">KelvaBank</text>
  </g>

  <text class="label" x="397" y="1405" text-anchor="middle">FOLDER OPEN</text>
  <text class="label" x="1187" y="1405" text-anchor="middle">FOLDER CLOSED</text>
  <text class="label" x="1187" y="1435" text-anchor="middle">FRONT</text>
</svg>
</body>
</html>
```